Company Mission & Values Poster

I'd like an A2 Portrait Poster displaying our company's Mission & Values.
See our website for our logo, fonts, mission & values.
https://valtemo.com.au/

Our Mission: Creating homes for abundant life
Values: Love, Thinking, Team, Zoe.

Some ideas to consider:
Mission as the Headline then
A logo for each of the 4 Values and the words

Target Market(s)

Myself & my team

Industry/Entity Type

Real Estate

Font styles to use
Other font styles liked:
• Company fonts as seen on our website

```html
<!DOCTYPE html>
<html lang="en">
<head>
<meta charset="utf-8">
<title>Valtemo — Mission &amp; Values Poster</title>
<link rel="stylesheet" href="https://fonts.googleapis.com/css2?family=Bodoni+Moda:ital,wght@0,400;1,400&family=Lexend:wght@200;400&family=Oswald:wght@600&family=Cormorant+Garamond:wght@500&display=swap">
<style>
  :root {
    --backdrop: #bcbdbf;
    --poster-green: #0c382d;
    --ink: #f3f1ec;
  }
  * { margin: 0; padding: 0; box-sizing: border-box; }
  html, body {
    width: 975px; height: 1200px; overflow: hidden;
    background: var(--backdrop);
  }
  .poster {
    position: absolute;
    left: 154px; top: 132px;
    width: 677px; height: 992px;
    background: var(--poster-green);
    color: var(--ink);
    text-align: center;
  }
  .line { position: absolute; left: 0; right: 0; line-height: 1; white-space: nowrap; }
  .mission-top {
    top: 70px;
    font-family: "Lexend", sans-serif; font-weight: 400;
    font-size: 30px; letter-spacing: 0.2px;
  }
  .mission-bottom {
    top: 116px;
    font-family: "Lexend", sans-serif; font-weight: 400;
    font-size: 30px;
  }
  .mission-bottom em {
    font-family: "Bodoni Moda", serif; font-style: italic;
    font-size: 36px;
  }
  .divider {
    position: absolute; left: 273px; width: 124px; height: 2px;
    background-image: radial-gradient(circle, var(--ink) 0.9px, transparent 1.1px);
    background-size: 10px 2px;
  }
  .divider-top { top: 196px; }
  .divider-bottom { top: 772px; }
  .value-bold {
    font-family: "Oswald", sans-serif; font-weight: 600;
    text-transform: uppercase; font-size: 88px; letter-spacing: -0.5px;
  }
  .value-love { top: 259px; }
  .value-team {
    top: 334px;
    font-family: "Lexend", sans-serif; font-weight: 200;
    font-size: 150px; letter-spacing: -4px;
  }
  .value-thinking { top: 496px; }
  .value-zoe {
    top: 570px;
    font-family: "Bodoni Moda", serif; font-weight: 400;
    font-size: 150px; letter-spacing: 2px;
  }
  .brand {
    position: absolute; left: 0; right: 0; top: 818px;
    display: flex; justify-content: center; align-items: center; gap: 10px;
  }
  .brand-dot {
    width: 18px; height: 18px; border-radius: 50%;
    border: 2px solid var(--ink);
  }
  .brand-name {
    font-family: "Cormorant Garamond", serif; font-weight: 500;
    font-size: 31px; letter-spacing: 3.5px; line-height: 1;
  }
</style>
</head>
<body>
  <main class="poster">
    <p class="line mission-top">Creating Home</p>
    <p class="line mission-bottom">for <em>Abundant Life</em></p>
    <div class="divider divider-top"></div>
    <h1 class="line value-bold value-love">Love</h1>
    <p class="line value-team">team</p>
    <p class="line value-bold value-thinking">Thinking</p>
    <p class="line value-zoe">zoe</p>
    <div class="divider divider-bottom"></div>
    <div class="brand">
      <span class="brand-dot"></span>
      <span class="brand-name">VALTEMO</span>
    </div>
  </main>
</body>
</html>
```